Design a "healthy, happy dog and cat" cheque/check background

I am looking for a few design concepts featuring a happy healthy dog and cat, that will be used as the background of a paper cheque/check.

This will require Photoshop and stock photos.

Here is the design brief: https://files.brivontel.net/sheet/48kQmZ2xTrWvLpN7aHcYeJ5uBdFsKo9GiRtXnVw3Lz/view?share=on

Colors

Designer to choose colors to be used in the design.

Requirements
Must have
• A happy dog and cat the main focus within the "empty" central part of the cheque/check, and a complementary background for the rest of the cheque, following the design guidelines in the attached google doc.

```html
<!DOCTYPE html>
<html lang="en">
<head>
<meta charset="utf-8">
<title>Happy Pets Personal Cheque</title>
<link rel="stylesheet" href="https://fonts.googleapis.com/css2?family=Arimo:wght@400;700&family=Share+Tech+Mono&display=swap">
<style>
  :root {
    --paper: #ffffff;
    --ink: #3d3d3d;
    --ink-dark: #111111;
    --park-top: #bdb9ab;
    --park-mid: #c9d6a2;
    --park-low: #a3c26a;
    --cat-grey: rgba(140, 142, 156, 0.55);
    --cat-fade: rgba(200, 201, 210, 0.35);
    --dog-cream: rgba(244, 234, 212, 0.7);
    --dog-shadow: rgba(226, 210, 178, 0.55);
    --dog-fade: rgba(250, 246, 236, 0.5);
    --field: #ffffff;
    --rule: #2a2a2a;
  }
  * { margin: 0; padding: 0; box-sizing: border-box; }
  html, body {
    width: 1200px; height: 544px; overflow: hidden;
    background: var(--paper);
    font-family: "Arimo", Arial, sans-serif;
    color: var(--ink);
  }
  .cheque { position: relative; width: 1200px; height: 544px; }
  .park-scene {
    position: absolute; left: 16px; top: 12px; width: 1166px; height: 402px;
    background: linear-gradient(180deg, var(--park-top) 0%, var(--park-mid) 38%, var(--park-low) 100%);
  }
  .pet { position: absolute; z-index: 1; }
  .pet-cat {
    left: 286px; top: 134px; width: 264px; height: 370px;
    border-radius: 46% 46% 22px 22px / 30% 30% 22px 22px;
    background: linear-gradient(180deg, var(--cat-grey) 0%, var(--cat-grey) 60%, var(--cat-fade) 100%);
  }
  .pet-dog {
    left: 566px; top: 14px; width: 304px; height: 530px;
    border-radius: 48% 48% 34px 34px / 26% 26% 34px 34px;
    background: linear-gradient(180deg, var(--dog-cream) 0%, var(--dog-shadow) 55%, var(--dog-fade) 100%);
  }
  .text { position: absolute; white-space: nowrap; z-index: 2; }
  .drawer-name { left: 58px; top: 62px; font-size: 21px; font-weight: 700; color: var(--ink); }
  .drawer-address { left: 58px; top: 85px; font-size: 20px; line-height: 22px; color: var(--ink); }
  .cheque-number { left: 1024px; top: 46px; font-size: 23px; font-weight: 700; color: var(--ink-dark); }
  .date-label { left: 784px; top: 111px; font-size: 20px; color: var(--ink-dark); }
  .date-boxes { position: absolute; left: 848px; top: 90px; display: flex; gap: 3px; z-index: 2; }
  .date-boxes span { width: 36px; height: 37px; background: var(--field); }
  .date-format { position: absolute; left: 848px; top: 131px; display: flex; gap: 3px; font-size: 13px; color: var(--ink-dark); z-index: 2; }
  .date-format span { width: 36px; text-align: center; }
  .payee-label { left: 56px; top: 190px; font-size: 13px; line-height: 13px; color: var(--ink-dark); }
  .dollar-sign { left: 960px; top: 187px; font-size: 28px; color: var(--ink-dark); }
  .amount-box { position: absolute; left: 1002px; top: 175px; width: 172px; height: 48px; background: var(--field); z-index: 2; }
  .amount-words { left: 918px; top: 253px; font-size: 14px; color: var(--ink-dark); }
  .bank-mark { position: absolute; left: 64px; top: 290px; width: 72px; height: 72px; border-radius: 50%; background: var(--ink-dark); z-index: 2; }
  .bank-name { left: 152px; top: 299px; font-size: 18px; font-weight: 700; color: var(--ink-dark); }
  .bank-address { left: 152px; top: 319px; font-size: 18px; line-height: 20px; color: var(--ink-dark); }
  .company-name { left: 808px; top: 333px; font-size: 14px; color: var(--ink-dark); }
  .memo-label { left: 54px; top: 383px; font-size: 12px; color: var(--ink-dark); }
  .security-badge {
    position: absolute; left: 1142px; top: 272px; width: 32px; height: 134px;
    border: 1.5px solid var(--ink); border-radius: 3px; z-index: 2;
  }
  .rules { position: absolute; left: 0; top: 0; z-index: 2; }
  .micr-line {
    left: 54px; top: 446px; font-family: "Share Tech Mono", "Courier New", monospace;
    font-size: 32px; letter-spacing: 9px; color: var(--ink-dark);
  }
</style>
</head>
<body>
<main class="cheque">
  <div class="park-scene" role="img" aria-label="Sunny park lawn with trees, softly blurred behind the pets"></div>
  <div class="pet pet-cat" role="img" aria-label="Faded grey shorthair cat resting its paws on the lower edge"></div>
  <div class="pet pet-dog" role="img" aria-label="Faded golden retriever puppy with its paws hanging over the lower edge"></div>

  <div class="text drawer-name">Northbay Cheques Personal Cheque</div>
  <div class="text drawer-address">15 Residential Street<br>Toronto, Ontario M1M 1M1</div>

  <div class="text cheque-number">101</div>
  <div class="text date-label">DATE</div>
  <div class="date-boxes"><span></span><span></span><span></span><span></span><span></span><span></span><span></span><span></span></div>
  <div class="date-format"><span>D</span><span>D</span><span>M</span><span>M</span><span>Y</span><span>Y</span><span>Y</span><span>Y</span></div>

  <div class="text payee-label">PAY TO THE<br>ORDER OF</div>
  <div class="text dollar-sign">$</div>
  <div class="amount-box"></div>
  <div class="text amount-words">100 DOLLARS</div>

  <div class="bank-mark"></div>
  <div class="text bank-name">Your Financial Institution</div>
  <div class="text bank-address">200 Finance Avenue<br>Your City, Your Province A1B 2CS</div>

  <div class="text company-name">Optional Company Name</div>
  <div class="text memo-label">MEMO</div>
  <div class="security-badge"></div>

  <svg class="rules" width="1200" height="544" viewBox="0 0 1200 544" aria-hidden="true">
    <g stroke="var(--rule)" stroke-width="1.2" fill="none">
      <polyline points="56,222 924,222 924,190"/>
      <polyline points="56,276 904,276 912,240"/>
      <line x1="54" y1="397" x2="590" y2="397"/>
      <line x1="692" y1="397" x2="1112" y2="397"/>
    </g>
  </svg>

  <div class="text micr-line">⑈101⑈ ⑆12345⑉678⑆ 12345⑉6789⑈</div>
</main>
</body>
</html>
```